Name card design for KOV mobile accessories company

KOV is an upmarket brand, we are looking for professional business card design.

the design should be neat and simple but giving a strong feeling.
should not be colorful. make it black/white/gray tone

Name:
Job title:
Contact no.:
company address: i would like the company address to be very small and thin.
link to social media profile:
company website:

*the company have no website yet
as the project is done please i also would like the font that use in design as well; for more further people in company need a business card:)
Updates

Thank you for all super fast submission :D they're all look cool!

i have just update my brief to make the statement clearer, please check it out :)
if you have any question please dont hesitate to ask.
i would like see more design from you! 
Keep it up!  :D

Target Market(s)

Company target are upmarket company distributor, such as Vordane and Pilto store.

Industry/Entity Type

Business

Font styles to use
Serif
Sans Serif
Other font styles liked:
• Formal and mordern

Colors
ffffff
eeeeee
d3d3d3
919191
474747
1b1b1b
000000
333333

Requirements
Must have
• The design must be professional clean and clear but also Strong and Modern!
text should be formal and mordern
Should not have
• No complicated design!

```html
<!DOCTYPE html>
<html lang="en">
<head>
<meta charset="utf-8">
<title>KOV Business Card</title>
<link href="https://fonts.googleapis.com/css2?family=Arimo:wght@400;500&display=swap" rel="stylesheet">
<style>
  :root {
    --page: #ffffff;
    --card-light: #ffffff;
    --card-dark: #1b1b1b;
    --ink: #333333;
    --text-soft: #c9c9c9;
    --text-muted: #a9a9a9;
    --mark-faint: #3c3c3c;
    --edge: #d3d3d3;
  }
  * { margin: 0; padding: 0; box-sizing: border-box; }
  html, body {
    width: 1200px;
    height: 1200px;
    overflow: hidden;
    background: var(--page);
    font-family: "Arimo", Arial, sans-serif;
  }
  .canvas {
    position: relative;
    width: 1200px;
    height: 1200px;
  }
  .card {
    position: absolute;
    left: 350px;
    width: 462px;
    overflow: hidden;
    box-shadow: 5px 7px 8px rgba(0, 0, 0, 0.22);
  }
  .card--front {
    top: 236px;
    height: 284px;
    background: var(--card-dark);
    border: 1px solid var(--edge);
  }
  .card--back {
    top: 654px;
    height: 282px;
    background: var(--card-dark);
  }
  .front-band {
    position: absolute;
    left: 0; top: 0;
    width: 100%;
    height: 116px;
    background: var(--card-light);
    display: flex;
    align-items: center;
    justify-content: center;
  }
  .brand-name {
    font-weight: 500;
    font-size: 46px;
    letter-spacing: 4px;
    color: var(--ink);
    line-height: 1;
    margin-top: -8px;
  }
  .contact {
    position: absolute;
    left: 0;
    width: 100%;
    text-align: center;
    font-style: normal;
    font-size: 13.5px;
    line-height: 18px;
    letter-spacing: 1.2px;
    font-weight: 400;
  }
  .card--front .contact {
    top: 229px;
    color: var(--text-soft);
  }
  .card--back .contact {
    top: 227px;
    color: var(--text-muted);
  }
  .brand-name--faint {
    position: absolute;
    left: 0;
    top: 66px;
    width: 100%;
    text-align: center;
    font-size: 84px;
    letter-spacing: 8px;
    color: var(--mark-faint);
    margin: 0;
  }
</style>
</head>
<body>
  <main class="canvas">
    <section class="card card--front" aria-label="Card front">
      <div class="front-band">
        <span class="brand-name">KOV</span>
      </div>
      <address class="contact">
        Harlow City, North State, 48 Elm Road<br>
        ph: 555-214-0387; mob: 010 472 6615
      </address>
    </section>

    <section class="card card--back" aria-label="Card back">
      <span class="brand-name brand-name--faint">KOV</span>
      <address class="contact">
        Email: hello@kovmobile.com<br>
        www.kovmobile.net
      </address>
    </section>
  </main>
</body>
</html>
```